Corporate Reception Invite (Harbor Social: SparkleLoft Edition)

I am looking for an invitation to use in Constant Contact for an upcoming reception. I have attached the company logo and a hero image from the reception location that may work well. Lastly, I attached an example from last year's invite for reference. Event details:

Harbor Social: SparkleLoft Edition @ ODP
October 23rd, 2023 from 6:00 - 8:00 pm
Orvessa at The Halvoring, Chicago
1174 W Pellingham St, Chicago, IL 60733
Join MVS & Friends for Cocktails & Conversation
Super casual - come and go as you please. Guests welcome.

Target Market(s)

Corporate audience

Font styles to use
Serif
Script
Other font styles liked:
• No strong preference, but want something elegant, sexy, and corporate

Colors
0054AA
0677BA
7BADD7
CADEEF
E8F1F8

Requirements
Must have
• MVS logo, event details, size: 600 x 1500 pixels

```html
<!DOCTYPE html>
<html lang="en">
<head>
<meta charset="UTF-8">
<title>Harbor Social: SparkleLoft Edition @ ODP</title>
<link rel="stylesheet" href="https://fonts.googleapis.com/css2?family=EB+Garamond:wght@400;600&family=Great+Vibes&display=swap">
<style>
  :root {
    --page-bg: #f2f2f2;
    --navy: #1f3a7a;
    --blue-deep: #0677ba;
    --blue-mid: #7badd7;
    --blue-script: #6fb6e6;
    --white: #ffffff;
    --photo-dark: #3a3f44;
    --photo-light: #c9d3dc;
    --photo-warm: #a88a6c;
  }
  * { margin: 0; padding: 0; box-sizing: border-box; }
  html, body { width: 1200px; height: 1200px; overflow: hidden; background: var(--page-bg); }
  .invite {
    position: absolute; left: 206px; top: 56px;
    width: 788px; height: 1088px;
    background: var(--navy); overflow: hidden;
  }
  .hero-photo {
    position: absolute; left: 0; top: 0; width: 788px; height: 470px;
    background:
      radial-gradient(ellipse at 45% 45%, var(--photo-warm) 0%, transparent 35%),
      linear-gradient(90deg, var(--photo-dark) 0%, var(--photo-light) 30%, #e6edf2 50%, var(--photo-light) 75%, var(--photo-dark) 100%);
  }
  .wave { position: absolute; left: 0; top: 0; width: 788px; height: 1088px; }
  .details { position: absolute; left: 0; top: 0; width: 788px; height: 1088px; color: var(--white); font-family: "EB Garamond", serif; }
  .line { position: absolute; left: 0; width: 100%; text-align: center; white-space: nowrap; }
  .event-title { top: 493px; font-size: 30px; line-height: 42px; font-weight: 600; }
  .event-date { top: 558px; font-size: 27px; line-height: 36px; }
  .event-date .dot { display: inline-block; margin: 0 14px; font-size: 20px; vertical-align: middle; }
  .venue { top: 610px; font-size: 26px; line-height: 34px; }
  .address { top: 651px; font-size: 26px; line-height: 34px; }
  .invite-script { font-family: "Great Vibes", cursive; color: var(--blue-script); font-size: 54px; line-height: 62px; }
  .script-one { top: 705px; }
  .script-two { top: 767px; }
  .note { top: 839px; font-size: 26px; line-height: 34px; }
  .host-mark {
    position: absolute; left: 296px; top: 929px; width: 195px; height: 114px;
    background: var(--white); border-radius: 28px;
    display: flex; align-items: center; justify-content: center; gap: 12px;
  }
  .host-mark .square { width: 26px; height: 26px; background: var(--navy); }
  .host-mark .name { font-family: "EB Garamond", serif; font-weight: 600; font-size: 40px; color: var(--navy); }
</style>
</head>
<body>
  <main class="invite">
    <div class="hero-photo" role="img" aria-label="Photo of wine glasses on a bar table at the reception venue"></div>
    <svg class="wave" viewBox="0 0 788 1088" aria-hidden="true">
      <defs>
        <linearGradient id="bandGradient" x1="0" y1="0" x2="1" y2="0">
          <stop offset="0" stop-color="#0677ba"/>
          <stop offset="0.35" stop-color="#7badd7"/>
          <stop offset="0.7" stop-color="#7badd7"/>
          <stop offset="1" stop-color="#0677ba"/>
        </linearGradient>
      </defs>
      <path d="M0,336 C200,318 420,392 560,420 C680,440 760,390 788,292 L788,1088 L0,1088 Z" fill="url(#bandGradient)"/>
      <path d="M0,344 C180,350 380,418 560,446 C680,462 760,440 788,403 L788,1088 L0,1088 Z" fill="#ffffff"/>
      <path d="M0,352 C180,358 380,426 560,455 C680,470 760,450 788,414 L788,1088 L0,1088 Z" fill="#1f3a7a"/>
    </svg>
    <section class="details">
      <h1 class="line event-title">Harbor Social: SparkleLoft Edition @ ODP</h1>
      <p class="line event-date"><span class="dot">&#9679;</span>October 23rd, 2023 from 6:00 - 8:00 pm<span class="dot">&#9679;</span></p>
      <p class="line venue">Orvessa at The Halvoring, Chicago</p>
      <p class="line address">1174 W Pellingham St, Chicago, IL 60733</p>
      <p class="line invite-script script-one">Join MVS &amp; Friends</p>
      <p class="line invite-script script-two">for Cocktails &amp; Conversation</p>
      <p class="line note">Super casual - come and go as you please. Guests welcome.</p>
    </section>
    <div class="host-mark"><span class="square"></span><span class="name">MVS</span></div>
  </main>
</body>
</html>
```